Looking for copywriting of the entire website + new selection of pictures

Hello,
My website's copy write is on the weaker side, so I'm looking for an entire re-do of my website's copy write. If you think a line is weak, re-write, otherwise you can leave it as is. We want our site to clearly explain what our events are, how they work, and why someone should sign up for them, while appealing to the hopeful, romantic, and nostalgic feelings of the visitors. Our speed dating events can be imagined as a modern day approach to the old-fashioned way of dating, where people got to know each other in person, away from the dating apps!! Additionally, I feel nearly all the existing pictures are rather weak, so please select entirely new pictures which give the website a less amateur feel, while retaining the playful nature of the brand. If there are areas where you think that section would benefit from no pictures at all, please communicate that.
Let me know if there are any further questions and thank you!
You can find the site at:
https://www.larkspindate.com
Industry/Entity Type
Speed Dating/Romance
Number of Pages Required
1 page
Look and feel
Each slider illustrates characteristics of the customer's brand and the style your logo design should communicate.

```html
<!DOCTYPE html>
<html lang="en">
<head>
<meta charset="utf-8">
<title>Larkspin Date — FAQs</title>
<link href="https://fonts.googleapis.com/css2?family=Roboto:wght@400;500;700&display=swap" rel="stylesheet">
<style>
:root{
  --ink:#2f2f2f;
  --pink:#ec1f73;
  --blue:#27a8c8;
  --line:#3a3a3a;
  --footer:#134b61;
  --star:#f5b80f;
  --white:#ffffff;
}
*{box-sizing:border-box;margin:0;padding:0}
html,body{width:1200px;height:2292px;overflow:hidden;background:var(--white)}
body{font-family:"Roboto",sans-serif;color:var(--ink);position:relative}
.faq-head{position:absolute;top:94px;left:0;width:1200px;text-align:center}
.faq-head h1{font-size:41px;font-weight:700;line-height:1}
.faq-head p{margin-top:33px;font-size:14.2px}
.faq-grid{position:absolute;top:251px;left:53px;width:1093px;display:flex;gap:54px;align-items:flex-start}
.faq-col{flex:1;border-top:1px solid var(--line)}
.faq-item{border-bottom:1px solid var(--line);padding:22px 0 18px}
.faq-q{display:flex;justify-content:space-between;align-items:center;color:var(--pink);font-weight:500;font-size:14.2px;line-height:18px}
.faq-q svg{width:16px;height:10px;margin-right:6px}
.faq-a{margin-top:15px;font-size:14.2px;line-height:22.4px}
.still{position:absolute;top:1146px;left:0;width:1200px;text-align:center}
.still h2{font-size:26.5px;font-weight:700}
.still p{margin-top:16px;font-size:14.2px}
.btn-outline{display:inline-block;margin-top:15px;width:107px;height:41px;border:1px solid var(--ink);border-radius:9px;line-height:39px;font-size:13px;color:var(--ink);text-decoration:none}
.reviews{position:absolute;top:1462px;left:53px;width:1093px}
.reviews h2{font-size:41px;font-weight:700;line-height:1.2}
.reviews h2 span{color:var(--blue)}
.reviews .lead{margin-top:23px;font-size:14.2px}
.review-row{margin-top:66px;display:flex;gap:45px}
.review{width:334px}
.stars{display:flex;gap:3px}
.stars svg{width:17px;height:17px;fill:var(--star)}
.review blockquote{margin-top:25px;font-size:16px;font-weight:700;line-height:23px}
.avatar{margin-top:25px;width:46px;height:46px;border-radius:50%}
.review cite{display:block;margin-top:15px;color:var(--pink);font-style:normal;font-weight:500;font-size:13px}
.slider-nav{margin-top:42px;display:flex;justify-content:space-between;align-items:center}
.dots{display:flex;gap:7px}
.dots i{width:6px;height:6px;border-radius:50%;background:#b8b8b8}
.dots i.on{background:var(--ink)}
.arrows{display:flex;gap:12px}
.arrows span{width:40px;height:40px;border:1px solid var(--ink);border-radius:50%;display:flex;align-items:center;justify-content:center}
.site-footer{position:absolute;top:1989px;left:0;width:1200px;height:303px;background:var(--footer);color:var(--white)}
.foot-top{position:absolute;top:70px;left:53px;width:1093px;height:50px;display:flex;align-items:center}
.brand{font-weight:700;font-size:15px;width:228px}
.contact{display:flex;align-items:center;gap:27px;font-size:13px}
.contact .strong{font-weight:700;display:flex;align-items:center;gap:16px}
.social{margin-left:auto;display:flex;gap:13px}
.social span{width:16px;height:16px;border-radius:50%;background:var(--pink)}
.foot-rule{position:absolute;top:192px;left:53px;width:1093px;border-top:1px solid #9db4be}
.legal{position:absolute;top:220px;left:0;width:1200px;text-align:center;font-size:11.5px}
.legal a{color:var(--white);margin-left:18px}
</style>
</head>
<body>

<header class="faq-head">
  <h1>FAQs</h1>
  <p>Find answers to common questions about our speed dating events, rules, and what to expect.</p>
</header>

<section class="faq-grid">
  <div class="faq-col">
    <div class="faq-item"><div class="faq-q">How does speed dating work?<svg viewBox="0 0 16 10"><path d="M1 1l7 7 7-7" fill="none" stroke="#ec1f73" stroke-width="1.8"/></svg></div>
      <p class="faq-a">Speed dating is a fun and efficient way to meet multiple potential partners in a short amount of time. Participants rotate from one table to another, engaging in brief conversations to get to know each other. At the end of the event, participants can indicate who they are interested in and if there is a mutual match, contact information is exchanged.</p></div>
    <div class="faq-item"><div class="faq-q">Is speed dating safe?<svg viewBox="0 0 16 10"><path d="M1 1l7 7 7-7" fill="none" stroke="#ec1f73" stroke-width="1.8"/></svg></div>
      <p class="faq-a">Yes, we prioritize the safety and comfort of our participants. Our events are held in secure venues and we have measures in place to ensure a respectful and enjoyable experience for everyone. We also provide guidelines and tips on how to make the most out of your speed dating experience.</p></div>
    <div class="faq-item"><div class="faq-q">What should I wear?<svg viewBox="0 0 16 10"><path d="M1 1l7 7 7-7" fill="none" stroke="#ec1f73" stroke-width="1.8"/></svg></div>
      <p class="faq-a">We recommend dressing in a way that makes you feel confident and comfortable. While there is no strict dress code, most participants opt for smart casual attire. It's important to make a good impression, so choose an outfit that reflects your personality and makes you feel great.</p></div>
    <div class="faq-item"><div class="faq-q">How long is each date?<svg viewBox="0 0 16 10"><path d="M1 1l7 7 7-7" fill="none" stroke="#ec1f73" stroke-width="1.8"/></svg></div>
      <p class="faq-a">Each date typically lasts around 10 minutes. This may vary slightly depending on the event and the number of participants. It may seem short, but it's enough time to get a sense of whether you'd like to continue the conversation and explore a potential connection.</p></div>
    <div class="faq-item"><div class="faq-q">What happens after the event?<svg viewBox="0 0 16 10"><path d="M1 1l7 7 7-7" fill="none" stroke="#ec1f73" stroke-width="1.8"/></svg></div>
      <p class="faq-a">After each date, just shoot a quick text to Larkspin Date indicating whether you're ready for a match or if it's a pass. It's a simple, interactive method to convey your interest and keep the connection going if the feeling is mutual.</p></div>
  </div>
  <div class="faq-col">
    <div class="faq-item"><div class="faq-q">How do I sign up for an event?<svg viewBox="0 0 16 10"><path d="M1 1l7 7 7-7" fill="none" stroke="#ec1f73" stroke-width="1.8"/></svg></div>
      <p class="faq-a">Signing up for an event is easy! Simply visit our website and browse the upcoming events in your area. Select the event you're interested in and follow the prompts to complete your registration. Don't wait too long, as spots fill up quickly!</p></div>
    <div class="faq-item"><div class="faq-q">How long do I have on each date?<svg viewBox="0 0 16 10"><path d="M1 1l7 7 7-7" fill="none" stroke="#ec1f73" stroke-width="1.8"/></svg></div>
      <p class="faq-a">Each date is a quick and enjoyable 10 minutes, offering you the opportunity to engage in a brief yet meaningful conversation and establish connections with potential matches. It's the perfect balance of efficiency and excitement, ensuring you make the most of every moment on your journey to find genuine connections.</p></div>
    <div class="faq-item"><div class="faq-q">What if I'm shy?<svg viewBox="0 0 16 10"><path d="M1 1l7 7 7-7" fill="none" stroke="#ec1f73" stroke-width="1.8"/></svg></div>
      <p class="faq-a">Speed dating can be a great way to break out of your shell and meet new people. Our events are designed to create a relaxed and comfortable atmosphere, and our friendly hosts are there to guide you through the process. Remember, everyone is in the same boat and looking to make connections, so don't be afraid to step out of your comfort zone.</p></div>
    <div class="faq-item"><div class="faq-q">Is there an age limit?<svg viewBox="0 0 16 10"><path d="M1 1l7 7 7-7" fill="none" stroke="#ec1f73" stroke-width="1.8"/></svg></div>
      <p class="faq-a">Our speed dating events are open to individuals of all ages, with specific events tailored to different age groups. This allows you to meet people within your preferred age range and increase the chances of finding a compatible match. Check our website for upcoming events in your age category.</p></div>
    <div class="faq-item"><div class="faq-q">How much do our events cost?<svg viewBox="0 0 16 10"><path d="M1 1l7 7 7-7" fill="none" stroke="#ec1f73" stroke-width="1.8"/></svg></div>
      <p class="faq-a">Secure your spot at a Larkspin Date event for just $24.99 per ticket, covering all service and payment processing fees. Our transparent and all-inclusive pricing ensures a delightful and immersive dating experience!</p></div>
  </div>
</section>

<section class="still">
  <h2>Still have questions?</h2>
  <p>Contact us for more information.</p>
  <a class="btn-outline" href="#">Contact Us</a>
</section>

<section class="reviews">
  <h2>What Others Say <span>About Us</span></h2>
  <p class="lead">Read what our previous participants have to say</p>
  <div class="review-row">
    <article class="review">
      <div class="stars"><svg viewBox="0 0 20 20"><path d="M10 1l2.7 5.8 6.3.7-4.7 4.3 1.3 6.2L10 14.9 4.4 18l1.3-6.2L1 7.5l6.3-.7z"/></svg><svg viewBox="0 0 20 20"><path d="M10 1l2.7 5.8 6.3.7-4.7 4.3 1.3 6.2L10 14.9 4.4 18l1.3-6.2L1 7.5l6.3-.7z"/></svg><svg viewBox="0 0 20 20"><path d="M10 1l2.7 5.8 6.3.7-4.7 4.3 1.3 6.2L10 14.9 4.4 18l1.3-6.2L1 7.5l6.3-.7z"/></svg><svg viewBox="0 0 20 20"><path d="M10 1l2.7 5.8 6.3.7-4.7 4.3 1.3 6.2L10 14.9 4.4 18l1.3-6.2L1 7.5l6.3-.7z"/></svg><svg viewBox="0 0 20 20"><path d="M10 1l2.7 5.8 6.3.7-4.7 4.3 1.3 6.2L10 14.9 4.4 18l1.3-6.2L1 7.5l6.3-.7z"/></svg></div>
      <blockquote>Speed dating is a game changer! I met my soulmate.</blockquote>
      <div class="avatar" role="img" aria-label="Portrait photo of Maren Holt" style="background:linear-gradient(135deg,#d9d6cf,#3b2a22)"></div>
      <cite>Maren Holt</cite>
    </article>
    <article class="review">
      <div class="stars"><svg viewBox="0 0 20 20"><path d="M10 1l2.7 5.8 6.3.7-4.7 4.3 1.3 6.2L10 14.9 4.4 18l1.3-6.2L1 7.5l6.3-.7z"/></svg><svg viewBox="0 0 20 20"><path d="M10 1l2.7 5.8 6.3.7-4.7 4.3 1.3 6.2L10 14.9 4.4 18l1.3-6.2L1 7.5l6.3-.7z"/></svg><svg viewBox="0 0 20 20"><path d="M10 1l2.7 5.8 6.3.7-4.7 4.3 1.3 6.2L10 14.9 4.4 18l1.3-6.2L1 7.5l6.3-.7z"/></svg><svg viewBox="0 0 20 20"><path d="M10 1l2.7 5.8 6.3.7-4.7 4.3 1.3 6.2L10 14.9 4.4 18l1.3-6.2L1 7.5l6.3-.7z"/></svg><svg viewBox="0 0 20 20"><path d="M10 1l2.7 5.8 6.3.7-4.7 4.3 1.3 6.2L10 14.9 4.4 18l1.3-6.2L1 7.5l6.3-.7z"/></svg></div>
      <blockquote>Larkspin Date is the best way to meet new people and find love.</blockquote>
      <div class="avatar" role="img" aria-label="Portrait photo of Clara Vance" style="background:linear-gradient(135deg,#6f9488,#c9b7a4)"></div>
      <cite>Clara Vance</cite>
    </article>
    <article class="review">
      <div class="stars"><svg viewBox="0 0 20 20"><path d="M10 1l2.7 5.8 6.3.7-4.7 4.3 1.3 6.2L10 14.9 4.4 18l1.3-6.2L1 7.5l6.3-.7z"/></svg><svg viewBox="0 0 20 20"><path d="M10 1l2.7 5.8 6.3.7-4.7 4.3 1.3 6.2L10 14.9 4.4 18l1.3-6.2L1 7.5l6.3-.7z"/></svg><svg viewBox="0 0 20 20"><path d="M10 1l2.7 5.8 6.3.7-4.7 4.3 1.3 6.2L10 14.9 4.4 18l1.3-6.2L1 7.5l6.3-.7z"/></svg><svg viewBox="0 0 20 20"><path d="M10 1l2.7 5.8 6.3.7-4.7 4.3 1.3 6.2L10 14.9 4.4 18l1.3-6.2L1 7.5l6.3-.7z"/></svg><svg viewBox="0 0 20 20"><path d="M10 1l2.7 5.8 6.3.7-4.7 4.3 1.3 6.2L10 14.9 4.4 18l1.3-6.2L1 7.5l6.3-.7z"/></svg></div>
      <blockquote>I had a fantastic experience at Larkspin Date. Highly recommended!</blockquote>
      <div class="avatar" role="img" aria-label="Portrait photo of Owen Pryce" style="background:linear-gradient(135deg,#cfcfcf,#2e2e2e)"></div>
      <cite>Owen Pryce</cite>
    </article>
  </div>
  <div class="slider-nav">
    <div class="dots"><i class="on"></i><i></i><i></i><i></i><i></i></div>
    <div class="arrows">
      <span><svg width="16" height="14" viewBox="0 0 16 14"><path d="M15 7H2M7 1L1 7l6 6" fill="none" stroke="#2f2f2f" stroke-width="1.6"/></svg></span>
      <span><svg width="16" height="14" viewBox="0 0 16 14"><path d="M1 7h13M9 1l6 6-6 6" fill="none" stroke="#2f2f2f" stroke-width="1.6"/></svg></span>
    </div>
  </div>
</section>

<footer class="site-footer">
  <div class="foot-top">
    <div class="brand">Larkspin Date</div>
    <div class="contact">
      <span class="strong"><svg width="16" height="16" viewBox="0 0 24 24"><path d="M6.6 10.8a15 15 0 006.6 6.6l2.2-2.2a1 1 0 011-.25 11.4 11.4 0 003.6.6 1 1 0 011 1V20a1 1 0 01-1 1A17 17 0 013 4a1 1 0 011-1h3.5a1 1 0 011 1c0 1.25.2 2.45.6 3.6a1 1 0 01-.25 1z" fill="#ec1f73"/></svg>(201) 555-0148</span>
      <span class="strong"><svg width="16" height="12" viewBox="0 0 16 12"><rect width="16" height="12" rx="1" fill="#ec1f73"/><path d="M1 1l7 5 7-5" fill="none" stroke="#134b61" stroke-width="1.3"/></svg>welcome@larkspindate.com</span>
      <span>Contact Us</span>
      <span>Events</span>
      <span>How it Works</span>
    </div>
    <div class="social" aria-label="Social links"><span role="img" aria-label="Photo sharing profile"></span><span role="img" aria-label="Short video profile"></span><span role="img" aria-label="Social network page"></span></div>
  </div>
  <div class="foot-rule"></div>
  <p class="legal">2024 LarkspinDate. All right reserved.<a href="#">Privacy Policy</a><a href="#">Terms of Service</a><a href="#">Cookies Settings</a></p>
</footer>

</body>
</html>
```